Need a web site design for a moving company

We need to re-design our website for our moving company based in New York. Our current web site (brightcartagepro.com) is very inconvenient for our customers to navigate and finding what they are looking for. We would like a web site which can have the customers fill up the Free Moving Quote after browsing it. So we want you to be creative with overall design and a quote form. We would love to target different locations, so we want our customers to be able to switch conveniently accordingly where they are located. We have a quorvi page with testimonials, which we wanted to be there as well (not just a text, and name. Boxes with pictures, profiles, just something creative and attractive). Attached is the logo, with two options(larkhaul -blue and larkhaul - orange, so the colors can be used accordingly or you can use your own colors if needed (if looks the best). If surfing the inner pages, we want our customers to be able to submit a quote request if needed.

Menu:
Home Services Moving Tips Testimonials About FAQ Blog Contact Us (doesn't have to be in order)

Inner Pages:
Services, Moving Tips, Testimonials, About, FAQ, Blog (moving quote is not necessary), Contact Us

Websites as references:
fetchporters.com
storvane.com
tranquilhaulers.com
tinycarters.com.au
urbantrekvans.com
wrenhaulage.co.uk
wecarrytoo.com

Reason: We are not in rush and really need someone who can read our brief throughout. We are looking for a new web site design. It doesn't have to an updated version of our current website as most of the submitted designs are. Also not all the content from a current website should be placed into a new one (depending on a style of a new layout or design you can partially copy paste some of the content). You can be as much creative as you can, making it clean looking, flat color with attractive user interface. If a menu is too long, we can skip some of them and place them in footer. The main things we are concerned about are quote form, option of location look up (switch between locations) and reviews (at least some part of the page should be dedicated to it). If you have any questions or if our brief is not clear, please let us know about it, Thank you

Moving Company

```html
<!DOCTYPE html>
<html lang="en">
<head>
<meta charset="utf-8">
<title>Bright Cartage — Moving Company</title>
<link rel="stylesheet" href="https://fonts.googleapis.com/css2?family=Roboto:wght@300;400;500;700;900&family=Libre+Baskerville:ital@1&family=Dancing+Script:wght@600&display=swap">
<style>
:root{
  --ink:#1c1c1c;
  --text:#555;
  --muted:#8a8a8a;
  --dark:#232323;
  --blue:#1a87d0;
  --blue-deep:#0b69b4;
  --blue-bar:#1d6fbe;
  --red:#ec3f55;
  --green:#2fae2a;
  --grey-bg:#f5f5f5;
  --line:#e2e2e2;
  --white:#fff;
}
*{box-sizing:border-box;margin:0;padding:0}
html,body{width:1200px;height:2507px;overflow:hidden}
body{position:relative;font-family:"Roboto",Arial,sans-serif;color:var(--text);background:var(--white)}
.abs{position:absolute}

/* top bar */
.topbar{left:0;top:0;width:1200px;height:62px;background:var(--dark)}
.brand{left:84px;top:18px;display:flex;align-items:center;gap:8px;color:var(--red);font-weight:700;font-size:17px;letter-spacing:.3px}
.brand-dot{width:22px;height:22px;border-radius:50%;background:var(--blue)}
.contact-chip{top:14px;height:34px;display:flex;align-items:center;gap:9px;color:var(--white);font-size:13px;font-weight:500}
.contact-chip .ico{width:26px;height:26px;border:1px solid #444;border-radius:3px;display:flex;align-items:center;justify-content:center}
.menu-panel{left:976px;top:0;width:150px;height:257px;background:var(--white);box-shadow:0 2px 8px rgba(0,0,0,.2);z-index:20}
.menu-close{position:absolute;left:64px;top:20px}
.menu-list{position:absolute;left:12px;top:70px;list-style:none;width:126px}
.menu-list li{display:flex;align-items:center;gap:9px;height:26.5px;font-size:10px;font-weight:700;color:var(--ink);border-bottom:1px solid #eee}
.menu-list li:last-child{border-bottom:0}
.menu-list li i{width:9px;height:9px;border-radius:2px;background:#555;display:block;flex:none}

/* hero */
.hero{left:0;top:62px;width:1200px;height:523px;background:linear-gradient(180deg,var(--blue) 0%,var(--blue-deep) 100%)}
.skyline{left:0;top:250px;width:1200px;height:273px;background:linear-gradient(180deg,rgba(255,255,255,0) 0%,rgba(0,40,90,.12) 100%)}
.hero-title{left:0;top:132px;width:1200px;text-align:center;color:var(--white);font-weight:300;font-size:42px}
.hero-title b{font-weight:900}
.hero-sub{left:0;top:187px;width:1200px;text-align:center;color:var(--white);font-family:"Libre Baskerville",Georgia,serif;font-style:italic;font-size:17px}
.hero-tag{left:0;top:238px;width:1200px;text-align:center;color:var(--white);font-weight:700;font-size:17px;letter-spacing:4px}
.btn-green{background:var(--green);color:var(--white);font-weight:700;font-size:11px;letter-spacing:2.5px;display:flex;align-items:center;justify-content:center;border-radius:2px}
.hero-btn{left:528px;top:281px;width:144px;height:37px}
.quote-label{left:0;top:398px;width:1200px;text-align:center;color:var(--white);font-weight:700;font-size:15px;letter-spacing:.5px}
.quote-label span{color:#ff8fa0}
.quote-label::before,.quote-label::after{content:"";display:inline-block;width:18px;height:1px;background:var(--white);vertical-align:middle;margin:0 12px}
.quote-form{left:137px;top:428px;width:924px;height:117px;background:var(--white);border-radius:4px;box-shadow:0 3px 10px rgba(0,0,0,.18)}
.field{position:absolute;border:1px solid #d6d6d6;border-radius:3px;font-size:10px;color:#999;padding:0 10px;display:flex;align-items:center;background:var(--white)}
.field.area{align-items:flex-start;padding-top:10px}
.btn-submit{position:absolute;left:832px;top:27px;width:67px;height:65px;background:var(--red);color:var(--white);font-size:12px;font-weight:700;border-radius:3px;display:flex;align-items:center;justify-content:center}

/* features */
.feature{top:665px;width:250px;text-align:center}
.feature svg{display:block;margin:0 auto 20px}
.feature h3{font-size:18px;font-weight:700;color:var(--ink);margin-bottom:10px}
.feature p{font-size:12px;line-height:1.35;color:#333;padding:0 28px}
.assured{left:0;top:860px;width:1200px;text-align:center;font-family:"Dancing Script",cursive;color:var(--red);font-size:15px}

/* services */
.services{left:0;top:919px;width:1200px;height:595px;background:var(--grey-bg);border-top:1px solid var(--line)}
.services-btn{left:473px;top:892px;width:254px;height:49px;font-size:11px}
.svc{width:400px}
.svc h4{font-size:15px;font-weight:700;color:var(--ink);margin-bottom:8px}
.svc p{font-size:11.5px;line-height:1.45;color:var(--muted);margin-bottom:10px}
.read-more{display:inline-block;border:1.5px solid var(--blue);color:var(--blue);font-size:9px;font-weight:700;padding:7px 6px;border-radius:2px}

/* coverage */
.covered{left:95px;top:1660px;font-size:28px;font-weight:900;letter-spacing:3px;color:var(--ink)}
.covered span{color:var(--red)}
.coverage-map{left:652px;top:1537px;width:426px;height:276px;background:linear-gradient(135deg,#3b82c4 0%,#2f76ba 70%,#cfcfcf 100%);border-radius:40px 60px 30px 70px}

/* testimonials */
.reviews{left:0;top:1843px;width:1200px;height:289px;background:linear-gradient(90deg,#d8cbb6 0%,#b99a72 40%,#c9ad86 70%,#8f7458 100%)}
.reviews-title{left:87px;top:1885px;font-size:31px;font-weight:700;color:var(--ink)}
.reviewer-photo{left:102px;top:1961px;width:116px;height:116px;border-radius:50%;background:#c98e6a;border:5px solid rgba(255,255,255,.8)}
.review-quote{left:242px;top:1968px;width:350px;font-size:14px;line-height:1.35;color:var(--white)}
.review-name{left:242px;top:2038px;font-size:14px;font-weight:700;color:#b5260f}
.signup{left:653px;top:1907px;width:462px;height:165px;background:rgba(255,255,255,.3)}
.signup h5{position:absolute;left:30px;top:34px;font-size:20px;font-weight:700;color:var(--white)}
.signup .email{position:absolute;left:30px;top:78px;width:263px;height:39px;background:var(--white);font-size:12px;color:#888;padding:0 12px;display:flex;align-items:center}
.signup .subscribe{position:absolute;left:306px;top:78px;width:127px;height:39px;background:var(--red);color:var(--white);font-size:11px;font-weight:700;letter-spacing:2px;display:flex;align-items:center;justify-content:center}

/* press */
.press-name{top:2172px;font-size:18px;color:#a8a8a8;text-align:center;transform:translateX(-50%);white-space:nowrap;font-weight:500}

/* footer */
.footer{left:0;top:2239px;width:1200px;height:224px;background:var(--dark)}
.notch{left:589px;top:2231px;width:0;height:0;border-left:8px solid transparent;border-right:8px solid transparent;border-bottom:8px solid var(--dark)}
.foot-col{top:2279px}
.foot-col h6{font-size:17px;font-weight:700;color:var(--white);margin-bottom:14px}
.foot-col ul{list-style:none}
.foot-col li{font-size:10.5px;color:#9a9a9a;line-height:20px}
.foot-col li.social{color:#3aa0e6;display:flex;align-items:center;gap:8px}
.foot-col li.social i{width:8px;height:8px;border-radius:50%;background:#3aa0e6;display:block}
.bottombar{left:0;top:2463px;width:1200px;height:44px;background:var(--blue-bar);display:flex;justify-content:center;align-items:center;gap:40px;color:var(--white);font-size:11px}
</style>
</head>
<body>

<header class="abs topbar"></header>
<div class="abs brand"><span class="brand-dot"></span>BRIGHT CARTAGE</div>
<div class="abs contact-chip" style="left:531px">
  <span class="ico"><svg width="12" height="12" viewBox="0 0 24 24"><path fill="#ccc" d="M6.6 10.8a15 15 0 0 0 6.6 6.6l2.2-2.2c.3-.3.7-.4 1-.2 1.1.4 2.3.6 3.6.6.6 0 1 .4 1 1V20c0 .6-.4 1-1 1A17 17 0 0 1 3 4c0-.6.4-1 1-1h3.5c.6 0 1 .4 1 1 0 1.3.2 2.5.6 3.6.1.3 0 .7-.2 1z"/></svg></span>
  Call Now : 888-555-0142
</div>
<div class="abs contact-chip" style="left:744px">
  <span class="ico"><svg width="12" height="12" viewBox="0 0 24 24"><rect x="2" y="5" width="20" height="14" rx="2" fill="none" stroke="#ccc" stroke-width="2"/><path d="M2 6l10 7 10-7" fill="none" stroke="#ccc" stroke-width="2"/></svg></span>
  info@brightcartagepro.com
</div>

<section class="abs hero"></section>
<div class="abs skyline" role="img" aria-label="Faint city skyline outline"></div>
<h1 class="abs hero-title">We are the professionals you can <b>TRUST</b></h1>
<p class="abs hero-sub">with your home or business move</p>
<p class="abs hero-tag">CALL. BOOK. MOVE.</p>
<div class="abs btn-green hero-btn">READ MORE</div>
<div class="abs quote-label">Get a <span>FREE</span> Quote</div>
<form class="abs quote-form">
  <div class="field" style="left:17px;top:20px;width:169px;height:35px">You Name</div>
  <div class="field" style="left:211px;top:20px;width:168px;height:35px">Email</div>
  <div class="field" style="left:17px;top:63px;width:169px;height:37px">Phone No</div>
  <div class="field" style="left:211px;top:63px;width:168px;height:37px;justify-content:space-between">Select Service<svg width="10" height="6" viewBox="0 0 10 6"><path d="M1 1l4 4 4-4" stroke="#222" stroke-width="1.8" fill="none"/></svg></div>
  <div class="field area" style="left:403px;top:20px;width:406px;height:80px">Your Reuirement Message!</div>
  <div class="btn-submit">Submit</div>
</form>

<nav class="abs menu-panel">
  <svg class="menu-close" width="22" height="22" viewBox="0 0 22 22"><path d="M2 2l18 18M20 2L2 20" stroke="#bbb" stroke-width="1.5"/></svg>
  <ul class="menu-list">
    <li><i></i>Services</li><li><i></i>Moving Tips</li><li><i></i>Testimonials</li><li><i></i>About</li><li><i></i>FAQ</li><li><i></i>Blog</li><li><i></i>Contact Us</li>
  </ul>
</nav>

<div class="abs feature" style="left:75px">
  <svg width="52" height="46" viewBox="0 0 52 46"><path d="M4 18L26 4l22 14v26H4z" fill="var(--red)"/><g fill="#fff"><rect x="12" y="20" width="6" height="6"/><rect x="23" y="20" width="6" height="6"/><rect x="34" y="20" width="6" height="6"/><rect x="12" y="30" width="6" height="6"/><rect x="34" y="30" width="6" height="6"/><rect x="23" y="32" width="6" height="12"/></g></svg>
  <h3>Residential Moving</h3><p>Tell us when, where, and what you're moving.</p>
</div>
<div class="abs feature" style="left:343px">
  <svg width="52" height="46" viewBox="0 0 52 46"><path d="M26 44S12 28 12 17a14 14 0 0 1 28 0c0 11-14 27-14 27z" fill="none" stroke="var(--red)" stroke-width="3"/><circle cx="26" cy="17" r="6" fill="var(--red)"/></svg>
  <h3>Local Moving</h3><p>See prices and user reviews, and choose a top-notch mover.</p>
</div>
<div class="abs feature" style="left:610px">
  <svg width="52" height="46" viewBox="0 0 52 46"><rect x="8" y="12" width="18" height="34" fill="var(--red)"/><rect x="28" y="2" width="16" height="44" fill="var(--red)"/><g fill="#fff"><rect x="12" y="17" width="4" height="4"/><rect x="18" y="17" width="4" height="4"/><rect x="12" y="26" width="4" height="4"/><rect x="18" y="26" width="4" height="4"/><rect x="32" y="8" width="3" height="4"/><rect x="38" y="8" width="3" height="4"/><rect x="32" y="18" width="3" height="4"/><rect x="38" y="18" width="3" height="4"/><rect x="32" y="28" width="3" height="4"/><rect x="38" y="28" width="3" height="4"/></g></svg>
  <h3>Commercial Moving</h3><p>Enter your details and lock in your guaranteed price.</p>
</div>
<div class="abs feature" style="left:864px">
  <svg width="76" height="46" viewBox="0 0 76 46" role="img" aria-label="Country outline icon"><rect x="4" y="6" width="68" height="34" rx="10" fill="var(--red)"/></svg>
  <h3>Interstate Moving</h3><p>That's it! Have a great move.</p>
</div>

<section class="abs services"></section>
<p class="abs assured">Best quality services assured!</p>
<div class="abs btn-green services-btn">OUR SERVICES</div>

<svg class="abs" style="left:106px;top:1023px" width="56" height="50" viewBox="0 0 56 50"><path d="M6 30l14-6 16 6 14-6v20l-14 6-16-6-14 6z" fill="none" stroke="var(--blue)" stroke-width="2.5"/><path d="M28 34S18 22 18 14a10 10 0 0 1 20 0c0 8-10 20-10 20z" fill="var(--blue)"/><circle cx="28" cy="14" r="4" fill="#fff"/></svg>
<div class="abs svc" style="left:197px;top:1012px"><h4>Local Moves</h4><p>Our experienced NYC movers can get your property relocated efficiently with minimal expenses.</p><span class="read-more">READ MORE</span></div>

<svg class="abs" style="left:660px;top:1040px" width="56" height="50" viewBox="0 0 56 50"><rect x="6" y="4" width="34" height="28" rx="3" fill="none" stroke="var(--blue)" stroke-width="2.5"/><path d="M14 22l9-8 9 8v8H14z" fill="none" stroke="var(--blue)" stroke-width="2"/><path d="M34 28c6 0 10 4 12 12l2 8H30l-4-8" fill="none" stroke="var(--blue)" stroke-width="2.5"/></svg>
<div class="abs svc" style="left:750px;top:1012px"><h4>Residential &amp; Commercial</h4><p>Whether you are moving your family or your business, our professional NYC movers will get the job done on time and on budget.</p><span class="read-more">READ MORE</span></div>

<svg class="abs" style="left:100px;top:1188px" width="66" height="56" viewBox="0 0 66 56"><path d="M12 32S3 22 3 14a9 9 0 0 1 18 0c0 8-9 18-9 18z" fill="var(--blue)"/><path d="M50 54S41 44 41 36a9 9 0 0 1 18 0c0 8-9 18-9 18z" fill="var(--blue)"/><path d="M14 36l8 8M26 46h10" stroke="var(--blue)" stroke-width="2.5" stroke-dasharray="3 3"/></svg>
<div class="abs svc" style="left:197px;top:1180px"><h4>Interstate/Long Distance Moves</h4><p>If you are planning on doing a long distance move, our team of New York movers can help you plan and execute it with no stress.</p><span class="read-more">READ MORE</span></div>

<svg class="abs" style="left:658px;top:1196px" width="60" height="50" viewBox="0 0 60 50"><path d="M8 16l22-8 22 8-22 8z M8 16v22l22 8 22-8V16 M30 24v22" fill="none" stroke="var(--blue)" stroke-width="2.5"/><path d="M8 16L2 24l22 8 6-8M52 16l6 8-22 8-6-8" fill="none" stroke="var(--blue)" stroke-width="2.5"/></svg>
<div class="abs svc" style="left:750px;top:1180px"><h4>Moving Supplies</h4><p>If you need to purchase moving or packing supplies, we can provide them to you at reasonable prices.</p><span class="read-more">READ MORE</span></div>

<svg class="abs" style="left:104px;top:1368px" width="60" height="56" viewBox="0 0 60 56"><rect x="18" y="4" width="22" height="18" fill="none" stroke="var(--blue)" stroke-width="2.5"/><rect x="4" y="24" width="24" height="26" fill="none" stroke="var(--blue)" stroke-width="2.5"/><rect x="30" y="24" width="24" height="26" fill="none" stroke="var(--blue)" stroke-width="2.5"/><path d="M29 4v8M16 24v8M42 24v8" stroke="var(--blue)" stroke-width="2.5"/></svg>
<div class="abs svc" style="left:197px;top:1358px"><h4>Storage</h4><p>Our New York movers can help you coordinate short or long term storage. We provide 1 month FREE of storage with any long distance moves.</p><span class="read-more">READ MORE</span></div>

<svg class="abs" style="left:664px;top:1374px" width="50" height="48" viewBox="0 0 50 48"><path d="M8 14a20 20 0 0 1 34 0" fill="none" stroke="var(--blue)" stroke-width="3"/><path d="M14 22l11-9 11 9v12H14z" fill="var(--blue)"/><path d="M4 34c8 0 10 4 18 4h14l8-6" fill="none" stroke="var(--blue)" stroke-width="3"/></svg>
<div class="abs svc" style="left:750px;top:1358px"><h4>Insurance</h4><p>Bright Cartage Inc. is fully licensed and insured. We offer a basic liability insurance or we will help you purchasing your insurance from a 3 rd party companies.</p><span class="read-more">READ MORE</span></div>

<h2 class="abs covered">WE'VE GOT YOU <span>COVERED</span></h2>
<div class="abs coverage-map" role="img" aria-label="Map of the United States showing served states in blue, home state New York highlighted in green"></div>

<section class="abs reviews" role="img" aria-label="Soft blurred interior photo backdrop in warm beige tones"></section>
<h2 class="abs reviews-title">What people are saying</h2>
<div class="abs reviewer-photo" role="img" aria-label="Portrait photo of the reviewer"></div>
<p class="abs review-quote">Simple. Quick. And to the point. I couldn't have been happier with the way everything turned out. I've been recommending carryswift to everyone!</p>
<p class="abs review-name">Daniel, NY</p>
<div class="abs signup">
  <h5>Signup for our email updates</h5>
  <div class="email">Email Address</div>
  <div class="subscribe">SUBSCRIBE</div>
</div>

<span class="abs press-name" style="left:175px;font-family:'Libre Baskerville',serif;font-style:italic;font-size:16px">The Daily Ledger</span>
<span class="abs press-name" style="left:371px;font-size:15px">Every Byte</span>
<span class="abs press-name" style="left:506px;font-size:20px;font-weight:900">Net Current</span>
<span class="abs press-name" style="left:677px;font-size:16px">Tech Harbor</span>
<span class="abs press-name" style="left:847px;font-family:'Libre Baskerville',serif;font-style:italic;font-size:19px">Capital Review</span>
<span class="abs press-name" style="left:1011px;font-size:14px;letter-spacing:1px">MORNING COURIER</span>

<footer class="abs footer"></footer>
<div class="abs notch"></div>
<div class="abs foot-col" style="left:95px"><h6>What we do</h6><ul><li>Local &amp; Long Distance Relocation</li><li>Free Online Reservation</li><li>Free Online Estimate</li><li>Moving Boxes &amp; Kits</li><li>Free Onsite Estimate</li><li>Full Packing &amp; Unpacking Services</li></ul></div>
<div class="abs foot-col" style="left:349px"><h6>Company</h6><ul><li>About</li><li>Careers</li><li>Press</li><li>Deals</li></ul></div>
<div class="abs foot-col" style="left:605px"><h6>Need Help?</h6><ul><li>FAQ</li><li>Contact</li></ul></div>
<div class="abs foot-col" style="left:899px"><h6>Connect</h6><ul><li class="social"><i></i>Pagebook</li><li class="social"><i></i>Chirpline</li></ul></div>
<div class="abs bottombar"><span>© Bright Cartage LLC 2014</span><span>1-855-555-0199</span><span>Privacy policy &nbsp;|&nbsp; Terms</span></div>

</body>
</html>
```